Lantern Voyages - Luxury, Theme, Guided Tours

Lan-voyages.example Lantern Voyages is being formed to create, sell and deliver to affluent baby boomers and mature adults, outstanding, memorable, boutique, luxury, guided theme tours to iconic North American destinations. These themes will revolve around activities and interests common to our target market, i.e. Culture, Culinary, Historic, Golf, Shopping etc. Our tours will include unique and enjoyable “wow” opportunities unavailable to guests were they to travel “on their own,” i.e. exclusive access, experiences and events, we arrange. Another critical component of our value proposition will be the camaraderie established among guests by marketing (and packaging) tours to specific markets. This will allow guests to tour, in small group sizes, with peers from their local community, with the opportunity to build new friendships that may flourish into the future.

Target Market(s)

Target Audience: Affluent, well-traveled, educated, sophisticated, fun, curious, brand-conscious, social senior/boomer ladies traveling with husband/partner or girlfriend(s)Brand Cohorts: Vellmarch, Quoro, Falbrook, Ostrelle

Industry/Entity Type

Tourism

Font styles to use
Serif

Colors
3176b5
ffffff
fbf289

Requirements
Must have
• "Open" area at top to add specific Tour Names and destinations - using design as template. Colors complementary to those used in logo.
• On Back:
• Luxury Guided Theme Adventures and Tours
• Designed Especially For Mature Adults - "Boomers"
• Small Group of Local Peers Traveling Together
• Executive Mini Coach Transportation
• Finest Boutique Hotels
• Award - Winning Restaurants and Chefs
• Exclusive and Unique Experiences, Events, Personalities and Tours
• Adventure and Tour Themes:
• Culinary & Cultural Trail
• Top Golf Resorts
• Historic Times, Sights and Cities
• Shopping!
• High Culture
• Nature
• Photography
• Music
• Wineries, Breweries and Distilleries
• Contact us today for all upcoming adventures and tours:
• Address: 2817 Mossgate Ln. Suite410 Raleigh, NC 27941 Phone: 919.555.0142 Email: info@lan-voyages.example www.lan-voyages.example 8am - 8pm EST
• Referrer name space
Nice to have
• antique compass, map

```html
<!DOCTYPE html>
<html lang="en">
<head>
<meta charset="utf-8">
<title>Lantern Voyages – Tour Features Rack Card</title>
<link rel="stylesheet" href="https://fonts.googleapis.com/css2?family=Cinzel:wght@400;700&display=swap">
<style>
  :root {
    --sky-blue: #1ac0f0;
    --deep-blue: #0070c0;
    --bullet-blue: #1a86d0;
    --sun-yellow: #fdb515;
    --ink: #2a2a2a;
    --heading-ink: #111111;
    --paper: #ffffff;
    --map-tint: #e9ebee;
  }
  * { margin: 0; padding: 0; box-sizing: border-box; }
  html, body { width: 1200px; height: 2613px; overflow: hidden; background: var(--paper); }
  .card {
    position: relative;
    width: 1200px;
    height: 2613px;
    background: var(--paper);
    font-family: "Cinzel", Georgia, serif;
    color: var(--ink);
  }
  .edge-band { position: absolute; left: 0; width: 1200px; height: 79px; display: block; }
  .edge-band--top { top: 0; }
  .edge-band--bottom { bottom: 0; transform: rotate(180deg); }

  .world-map {
    position: absolute;
    left: 15px; top: 1341px;
    width: 1135px; height: 552px;
    background: radial-gradient(ellipse at 50% 45%, var(--map-tint) 0%, rgba(233,235,238,0.55) 55%, rgba(255,255,255,0) 80%);
  }

  .feature-list { list-style: none; }
  .feature {
    position: absolute;
    left: 119px;
    font-size: 35px;
    line-height: 42px;
    white-space: nowrap;
  }
  .feature::before {
    content: "";
    position: absolute;
    left: -37px; top: 12px;
    width: 17px; height: 17px;
    border: 3px solid var(--bullet-blue);
    transform: rotate(45deg);
  }

  .contact-heading {
    position: absolute;
    left: 0; top: 1945px;
    width: 1200px;
    text-align: center;
    font-weight: 700;
    font-size: 45px;
    line-height: 58px;
    color: var(--heading-ink);
  }
  .contact-heading span { display: block; }
  .accent-bar { position: absolute; top: 2016px; height: 34px; }
  .accent-bar--left { left: 0; width: 260px; background: var(--sky-blue); }
  .accent-bar--right { right: 0; width: 262px; background: var(--deep-blue); }
  .rule { position: absolute; left: 0; top: 2059px; width: 1200px; height: 12px; background: var(--sun-yellow); }

  .contact-list { list-style: none; }
  .contact-item {
    position: absolute;
    left: 52px;
    display: flex;
    align-items: center;
    gap: 12px;
    font-size: 34px;
    line-height: 40px;
    white-space: nowrap;
  }
  .contact-icon { width: 30px; height: 30px; flex: none; }
</style>
</head>
<body>
<main class="card">

  <svg class="edge-band edge-band--top" viewBox="0 0 1200 79" aria-hidden="true">
    <polygon points="0,0 495,0 455,79 0,79" fill="var(--sky-blue)"/>
    <polygon points="462,79 490,79 530,0 502,0" fill="var(--sun-yellow)"/>
    <polygon points="508,79 536,79 576,0 548,0" fill="var(--sun-yellow)"/>
    <polygon points="554,79 582,79 622,0 594,0" fill="var(--sun-yellow)"/>
    <polygon points="600,79 628,79 668,0 640,0" fill="var(--sun-yellow)"/>
    <polygon points="646,79 674,79 714,0 686,0" fill="var(--sun-yellow)"/>
    <polygon points="700,79 740,0 1200,0 1200,79" fill="var(--deep-blue)"/>
  </svg>

  <div class="world-map" role="img" aria-label="Faint dotted world map in light grey behind the theme list"></div>

  <ul class="feature-list">
    <li class="feature" style="top:171px">Luxury Guided Theme Adventures and Tours</li>
    <li class="feature" style="top:273px">Designed Especially For Mature Adults - "Boomers"</li>
    <li class="feature" style="top:373px">Small Group of Local Peers Traveling Together</li>
    <li class="feature" style="top:473px">Executive Mini Coach Transportation</li>
    <li class="feature" style="top:572px">Finest Boutique Hotels</li>
    <li class="feature" style="top:674px">Award - Winning Restaurants and Chefs</li>
    <li class="feature" style="top:753px">Exclusive and Unique Experiences, Events,<br>Personalities and Tours</li>
    <li class="feature" style="top:874px">Adventure and Tour Themes</li>
    <li class="feature" style="top:974px">Culinary &amp; Cultural Trail</li>
    <li class="feature" style="top:1074px">Top Golf Resorts</li>
    <li class="feature" style="top:1175px">Historic Times, Sights and Cities</li>
    <li class="feature" style="top:1275px">Shopping</li>
    <li class="feature" style="top:1375px">High Culture</li>
    <li class="feature" style="top:1475px">Nature</li>
    <li class="feature" style="top:1575px">Photography</li>
    <li class="feature" style="top:1675px">Music</li>
    <li class="feature" style="top:1774px">Wineries, Breweries and Distilleries</li>
  </ul>

  <div class="accent-bar accent-bar--left"></div>
  <div class="accent-bar accent-bar--right"></div>
  <h2 class="contact-heading"><span>Contact us today for all upcoming</span><span>adventures and tours</span></h2>
  <div class="rule"></div>

  <ul class="contact-list">
    <li class="contact-item" style="top:2120px">
      <svg class="contact-icon" viewBox="0 0 30 30" aria-hidden="true"><circle cx="15" cy="15" r="15" fill="var(--sun-yellow)"/><path d="M15 7a5.5 5.5 0 0 0-5.5 5.5C9.5 17 15 23 15 23s5.5-6 5.5-10.5A5.5 5.5 0 0 0 15 7z" fill="#fff"/><circle cx="15" cy="12.5" r="2" fill="var(--sun-yellow)"/></svg>
      <span>2817 Mossgate Ln. Suite410 Raleigh, NC 27941</span>
    </li>
    <li class="contact-item" style="top:2180px">
      <svg class="contact-icon" viewBox="0 0 30 30" aria-hidden="true"><circle cx="15" cy="15" r="15" fill="var(--sun-yellow)"/><rect x="11" y="7" width="8" height="16" rx="1.5" fill="#fff"/><rect x="12.5" y="9" width="5" height="10" fill="var(--sun-yellow)"/></svg>
      <span>919.555.0142</span>
    </li>
    <li class="contact-item" style="top:2241px">
      <svg class="contact-icon" viewBox="0 0 30 30" aria-hidden="true"><circle cx="15" cy="15" r="15" fill="var(--sun-yellow)"/><rect x="8" y="10" width="14" height="10" fill="#fff"/><path d="M8 10l7 6 7-6" fill="none" stroke="var(--sun-yellow)" stroke-width="1.5"/></svg>
      <span>info@lan-voyages.example</span>
    </li>
    <li class="contact-item" style="top:2301px">
      <svg class="contact-icon" viewBox="0 0 30 30" aria-hidden="true"><circle cx="15" cy="15" r="15" fill="var(--sun-yellow)"/><circle cx="15" cy="15" r="7.5" fill="none" stroke="#fff" stroke-width="1.8"/><path d="M7.5 15h15M15 7.5c-3 3-3 12 0 15M15 7.5c3 3 3 12 0 15" fill="none" stroke="#fff" stroke-width="1.5"/></svg>
      <span>www.lan-voyages.example</span>
    </li>
  </ul>

  <svg class="edge-band edge-band--bottom" viewBox="0 0 1200 79" aria-hidden="true">
    <polygon points="0,0 495,0 455,79 0,79" fill="var(--sky-blue)"/>
    <polygon points="462,79 490,79 530,0 502,0" fill="var(--sun-yellow)"/>
    <polygon points="508,79 536,79 576,0 548,0" fill="var(--sun-yellow)"/>
    <polygon points="554,79 582,79 622,0 594,0" fill="var(--sun-yellow)"/>
    <polygon points="600,79 628,79 668,0 640,0" fill="var(--sun-yellow)"/>
    <polygon points="646,79 674,79 714,0 686,0" fill="var(--sun-yellow)"/>
    <polygon points="700,79 740,0 1200,0 1200,79" fill="var(--deep-blue)"/>
  </svg>

</main>
</body>
</html>
```